Card design for Heating and Cooling company

this is for a heating and cooling company we recently updated our logo and need to update our cards. We attached our logo so you can incorporate it into the card. We specialize in residential and commercial furnace and air condition repairs. Have been in business since 2014.

Phone number 555.284.9137

We need the following phrases
:Repairs, Installations, and maintenance
:Quality work at reasonable prices
:residential/commercial
:Licensed &Insured
:Email Pinegrovehvac47@mailbox-example.com
Name: Teodor K (Ted)
Also on back side I would like my logo with wording :Thank you for your business and refferal

Industry/Entity Type

Hvac

Contact Information for Business Card

:residential/commercial
:Licensed & Insured
Name: Teodor K (Ted)
Number:555.284.9136

Requirements
Must have
• Blue and red colors
Nice to have
• Maybe a pic of a furnace or air conditioner

```html
<!DOCTYPE html>
<html lang="en">
<head>
<meta charset="utf-8">
<title>Pinegrove Heating &amp; Cooling – Business Card</title>
<link href="https://fonts.googleapis.com/css2?family=Montserrat:wght@600;700;800&family=Open+Sans:wght@400;600&family=Dancing+Script:wght@600&display=swap" rel="stylesheet">
<style>
  :root {
    --page-bg: #e9e6e1;
    --card-bg: #ffffff;
    --ink: #1a1a1a;
    --red: #e0262b;
    --blue: #2ba6e3;
    --orange: #f7a21b;
    --rule: #2a2a2a;
    --shadow: 0 6px 16px rgba(0,0,0,0.35);
  }
  * { box-sizing: border-box; margin: 0; padding: 0; }
  html, body { width: 900px; height: 1200px; overflow: hidden; }
  body {
    background: var(--page-bg);
    position: relative;
    font-family: "Open Sans", Arial, sans-serif;
    color: var(--ink);
  }
  .card {
    position: absolute;
    left: 86px;
    width: 734px;
    height: 429px;
    border-radius: 24px;
    background: var(--card-bg);
    box-shadow: var(--shadow);
    overflow: hidden;
  }
  .card--front { top: 131px; }
  .card--back { top: 633px; }

  /* Front */
  .contact { position: absolute; left: 42px; top: 52px; }
  .contact__name {
    font-family: "Montserrat", Arial, sans-serif;
    font-weight: 700; font-size: 21px; letter-spacing: 0.2px;
  }
  .contact__title { color: var(--red); font-size: 17px; margin-top: 2px; }
  .contact__list { list-style: none; margin-top: 20px; }
  .contact__item {
    display: flex; align-items: center; gap: 6px;
    font-size: 17px; line-height: 27px;
  }
  .contact__icon { width: 19px; height: 19px; flex: none; }

  .brand {
    position: absolute; left: 370px; top: 120px; width: 330px;
    display: flex; flex-direction: column; align-items: center; gap: 14px;
  }
  .brand__dot {
    width: 46px; height: 46px; border-radius: 50%; background: var(--blue);
  }
  .brand__name {
    font-family: "Montserrat", Arial, sans-serif;
    font-weight: 800; font-size: 40px; line-height: 1.05;
    color: var(--ink); text-align: center; text-transform: uppercase;
  }
  .brand__name span { display: block; font-size: 15px; letter-spacing: 4px; margin-top: 6px; }

  .services { position: absolute; left: 42px; top: 324px; }
  .services__list {
    font-family: "Open Sans", Arial, sans-serif;
    font-weight: 600; font-size: 17px;
  }
  .services__sep { color: var(--blue); margin: 0 4px; }
  .services__tagline { color: var(--red); font-size: 16px; margin-top: 3px; }

  .footer-line {
    position: absolute; left: 42px; right: 42px; top: 377px;
    border-top: 1.5px solid var(--rule);
    display: flex; justify-content: space-between;
    padding-top: 5px; font-size: 15px;
  }

  /* Back */
  .hero {
    position: absolute; inset: 0 0 52px 0;
    background: linear-gradient(90deg, #a9acaf 0%, #d8dadb 28%, #f3f3f1 50%, #f7f4ef 75%, #e4d4be 100%);
  }
  .hero__brand {
    position: absolute; left: 0; right: 0; top: 120px;
    display: flex; flex-direction: column; align-items: center; gap: 12px;
  }
  .stripe {
    position: absolute; left: 0; right: 0; bottom: 52px; height: 6px;
    background: linear-gradient(90deg, var(--red), var(--orange) 40%, var(--blue));
    border-top: 2px solid #fff;
  }
  .thanks {
    position: absolute; left: 0; right: 0; bottom: 0; height: 52px;
    background: linear-gradient(90deg, var(--orange) 0%, #ea5a2a 30%, #b2556b 60%, var(--blue) 100%);
    display: flex; align-items: center; justify-content: center;
    font-family: "Dancing Script", "Brush Script MT", cursive;
    font-weight: 600; font-size: 27px; color: #fff;
  }
</style>
</head>
<body>

<section class="card card--front" aria-label="Business card front">
  <div class="contact">
    <h1 class="contact__name">TEODOR K (TED)</h1>
    <p class="contact__title">Managing Director</p>
    <ul class="contact__list">
      <li class="contact__item">
        <svg class="contact__icon" viewBox="0 0 20 20" aria-hidden="true">
          <rect width="20" height="20" rx="4" fill="#e86b57"/>
          <path d="M6 4.5l2 2.4-1.2 1.5c.9 1.8 2.3 3.2 4.1 4.1l1.5-1.2 2.4 2-1.2 2c-4.8-.3-8.4-3.9-8.7-8.7z" fill="#fff"/>
        </svg>
        555.284.9136
      </li>
      <li class="contact__item">
        <svg class="contact__icon" viewBox="0 0 20 20" aria-hidden="true">
          <rect width="20" height="20" rx="4" fill="#e86b57"/>
          <rect x="4" y="6" width="12" height="8.5" fill="#fff"/>
          <path d="M4 6l6 5 6-5" fill="none" stroke="#e86b57" stroke-width="1.3"/>
        </svg>
        Pinegrovehvac47@mailbox-example.com
      </li>
    </ul>
  </div>

  <div class="brand">
    <div class="brand__dot"></div>
    <p class="brand__name">Pinegrove<span>Heating &amp; Cooling</span></p>
  </div>

  <div class="services">
    <p class="services__list">Repairs<span class="services__sep">•</span>Installations<span class="services__sep">•</span>Maintenance</p>
    <p class="services__tagline">Quality work at reasonable prices</p>
  </div>

  <div class="footer-line">
    <span>Residential • Commercial</span>
    <span>Licensed &amp; Insured</span>
  </div>
</section>

<section class="card card--back" aria-label="Business card back">
  <div class="hero" role="img" aria-label="Photo of a furnace and water heater installation beside a bright living room with a wall-mounted air conditioner and airflow swirls"></div>
  <div class="hero__brand">
    <div class="brand__dot"></div>
    <p class="brand__name">Pinegrove<span>Heating &amp; Cooling</span></p>
  </div>
  <div class="stripe"></div>
  <p class="thanks">Thank you for your business and refferal</p>
</section>

</body>
</html>
```